Security Services Business Card

Looking for a clean modern style business card design for a residential and commercial security solutions provider. We install and service the following
security alarm, access control, video surveillance and fire alarm. Attached are the front and back of our current business cards in PSD file format.

Target Market(s)

Security alarm clients in the commercial and residential markets

Industry/Entity Type

Security Service

Contact Information for Business Card

We are open to designers suggestion and or design ideas.

Font styles to use
Serif
Sans Serif

Colors
3276b5
33a6d7
fffefd

Requirements
Must have
• Must have company logo , first and last name , phone number , web and email address, ect....

```html
<!DOCTYPE html>
<html lang="en">
<head>
<meta charset="utf-8">
<title>Veritrax Business Card</title>
<link href="https://fonts.googleapis.com/css2?family=Roboto:wght@400;500;700;900&display=swap" rel="stylesheet">
<style>
  :root {
    --brand-blue: #2777b5;
    --paper: #ffffff;
    --ink: #1f1f1f;
    --backdrop: #d2d2d2;
  }
  * { margin: 0; padding: 0; box-sizing: border-box; }
  html, body { width: 1200px; height: 1059px; overflow: hidden; }
  body {
    position: relative;
    background: var(--backdrop);
    font-family: "Roboto", Arial, sans-serif;
    color: var(--ink);
  }
  .card {
    position: absolute;
    border-radius: 18px;
    overflow: hidden;
  }
  .card--front { left: 257px; top: 100px; width: 687px; height: 391px; background: var(--paper); }
  .card--back { left: 253px; top: 537px; width: 694px; height: 394px; background: var(--brand-blue); }

  .brand-name {
    position: absolute;
    font-weight: 900;
    letter-spacing: 0.5px;
    line-height: 1;
    display: flex;
    align-items: center;
  }
  .brand-mark { border-radius: 50%; flex: none; }
  .card--front .brand-name { left: 48px; top: 170px; font-size: 46px; color: var(--brand-blue); gap: 12px; }
  .card--front .brand-mark { width: 16px; height: 16px; background: var(--brand-blue); }

  .divider { position: absolute; left: 342px; top: 115px; width: 2px; height: 161px; background: var(--brand-blue); }

  .contact { position: absolute; left: 372px; top: 110px; }
  .contact__name { font-size: 24px; font-weight: 700; color: var(--brand-blue); line-height: 1.1; }
  .contact__title { font-size: 16px; margin-top: 2px; }
  .contact__address { font-size: 16px; line-height: 20px; margin-top: 16px; }
  .contact__list { list-style: none; margin-top: 8px; font-size: 16px; }
  .contact__list li { display: flex; align-items: center; gap: 6px; height: 20.5px; }
  .contact__list svg { width: 12px; height: 12px; fill: var(--brand-blue); flex: none; }

  .card--back .brand-name { left: 0; right: 0; top: 160px; justify-content: center; font-size: 86px; color: var(--paper); gap: 20px; }
  .card--back .brand-mark { width: 26px; height: 26px; background: var(--paper); }

  .services { position: absolute; left: 0; right: 0; top: 294px; text-align: center; color: var(--paper); }
  .services__heading {
    display: inline-block;
    font-size: 20px;
    font-weight: 700;
    letter-spacing: 0.3px;
    padding-bottom: 8px;
    border-bottom: 1.5px solid var(--paper);
  }
  .services__list { list-style: none; display: flex; justify-content: center; gap: 12px; margin-top: 12px; font-size: 20px; }
  .services__list li::before { content: "• "; font-size: 15px; vertical-align: 2px; }
</style>
</head>
<body>
  <section class="card card--front">
    <div class="brand-name"><span class="brand-mark"></span>Veritrax</div>
    <div class="divider"></div>
    <div class="contact">
      <div class="contact__name">DANIEL HOLLIS</div>
      <div class="contact__title">Owner/CEO</div>
      <div class="contact__address">4720 Lakeview Ave # 310,<br>Bay Harbor Ohio 44098</div>
      <ul class="contact__list">
        <li><svg viewBox="0 0 24 24"><path d="M6.6 10.8a15.1 15.1 0 0 0 6.6 6.6l2.2-2.2c.3-.3.7-.4 1-.2 1.1.4 2.3.6 3.6.6.6 0 1 .4 1 1V20c0 .6-.4 1-1 1A17 17 0 0 1 3 4c0-.6.4-1 1-1h3.5c.6 0 1 .4 1 1 0 1.3.2 2.5.6 3.6.1.3 0 .7-.2 1z"/></svg>555.014.2290 ext 112</li>
        <li><svg viewBox="0 0 24 24"><path d="M2 5h20v14H2zm2 2v.5l8 5 8-5V7zm0 3v7h16v-7l-8 5z"/></svg>contact@veritraxsecure.com</li>
        <li><svg viewBox="0 0 24 24"><path d="M12 2a10 10 0 1 0 0 20 10 10 0 0 0 0-20zm-1 17.9A8 8 0 0 1 4.2 10.2L9 15v1c0 1.1.9 2 2 2zm6.9-2.5c-.3-.8-1-1.4-1.9-1.4h-1v-3c0-.6-.4-1-1-1H8v-2h2c.6 0 1-.4 1-1V7h2c1.1 0 2-.9 2-2v-.4a8 8 0 0 1 2.9 12.8z"/></svg>www.veritraxsecure.com</li>
      </ul>
    </div>
  </section>

  <section class="card card--back">
    <div class="brand-name"><span class="brand-mark"></span>Veritrax</div>
    <div class="services">
      <h2 class="services__heading">WE INSTALL AND SERVICE</h2>
      <ul class="services__list">
        <li>Security Alarm</li>
        <li>Access Control</li>
        <li>Video Surveillance</li>
        <li>Fire Alarm</li>
      </ul>
    </div>
  </section>
</body>
</html>
```